Flyer: helping to close the Global Digital Divide- V20 project.

We need a flyer designing for a nonprofit (www.brambleloop.org) based in Washington DC and London. We help to connect communities that have no internet so that they can get access to the health, educational, socio-economic benefits of internet connectivity. The project is ‘V20’ – internet for the Vital 20%.
The flyer will be sent to major corporations, governments, major universities, and the like.
The first half of the flyer will be design rich and incorporate the words (on the attached V20 document) in a creative and appealing way using design and color contrasts to highlight important points. The V20 Logo is attached also. I have also attached a similar but different PLRT document to give some ideas.
The second half of the flyer will be an MOU (Memorandum of Understanding) for the corporations to sign. This needs to be simple and look professional.
It is very important that we can change the words in the flyer once the design is complete without having to go back to the designer every time.

```html
<!DOCTYPE html>
<html lang="en">
<head>
<meta charset="utf-8">
<title>The V20 Charter</title>
<link href="https://fonts.googleapis.com/css2?family=Montserrat:wght@400;500;600;700;800;900&display=swap" rel="stylesheet">
<style>
:root{
  --blue:#0a7fc4;
  --heading-blue:#1277c0;
  --ink:#2b2b2b;
  --muted:#444;
  --magenta:#c4007a;
  --gold:#a9820a;
  --green:#128a6e;
  --plum:#2a0a3a;
  --highlight-box:#c3e1f0;
  --paper:#ffffff;
  --bg:#ffffff;
}
*{box-sizing:border-box;margin:0;padding:0}
html,body{width:1200px;height:1200px;overflow:hidden;background:var(--bg)}
body{position:relative;font-family:'Montserrat',sans-serif;color:var(--ink)}
.page{position:absolute;width:364px;height:514px;background:var(--paper);overflow:hidden;
  box-shadow:0 6px 22px rgba(0,0,0,.16)}
.p1{left:50px;top:90px}.p2{left:430px;top:89px}
.p3{left:49px;top:626px}.p4{left:427px;top:628px}.p5{left:808px;top:628px}
.page-head .bar{position:absolute;left:0;top:0;width:15px;height:52px;background:var(--blue)}
.page-head .title{position:absolute;left:25px;top:24px;font-weight:900;font-size:19px;color:#111;letter-spacing:-.2px}
.page-head .subtitle{position:absolute;left:26px;top:45px;font-size:5px;color:#333}
.brand-name{position:absolute;right:28px;top:27px;font-weight:700;font-size:15px;color:var(--ink)}
.body{position:absolute;left:26px;right:26px;font-size:7.5px;line-height:8.7px;color:var(--muted)}
.body p{margin-bottom:4px;text-align:justify}
.slogan{text-align:center;font-weight:700;font-size:12.5px;line-height:15px;color:#111;margin:0 0 18px}
.section-title{color:var(--heading-blue);font-weight:700;font-size:10px;margin:0 0 3px}
.tag{color:#fff;padding:0 1px}
.tag.m{background:var(--magenta)}.tag.g{background:var(--gold)}.tag.gr{background:var(--green)}.tag.pl{background:var(--plum)}
.tick{font-size:6px;color:#111}
.pattern{position:absolute;background:linear-gradient(135deg,rgba(10,127,196,.10),rgba(10,127,196,0))}
.cta-band{position:absolute;left:0;right:0;bottom:0;height:80px;background:var(--blue);padding:7px 26px;color:#d7ecf8;font-size:7.5px;line-height:8.7px}
.cta-band h2{color:#fff;font-size:11px;font-weight:700;border-bottom:1px solid #fff;display:inline-block;padding-bottom:2px;margin-bottom:5px}
.cta-band b{color:#fff}
.mou-title{text-align:center;font-weight:700;font-size:10.5px;color:#111;margin:0 0 13px}
.lead{font-weight:600;color:#111;font-size:7.5px;margin-bottom:1px}
.sign-table{width:266px;margin:12px auto 12px;border-collapse:collapse;font-size:7.2px;border:1.5px solid #111}
.sign-table th{background:#111;color:#fff;text-align:left;font-weight:500;padding:4px 5px 5px}
.sign-table td{border:1px solid #111;padding:1px 5px;vertical-align:top;height:11px}
.sign-table td.signed{height:44px}
.agree-title{font-weight:700;color:#111;font-size:7.3px;margin:0 0 2px}
.clauses{list-style:none;font-size:6.7px;line-height:7.45px}
.clauses li{display:flex;gap:8px;margin-bottom:7px;text-align:justify}
.clauses .n{flex:0 0 10px}
.exhibit-title{text-align:center;font-size:7px;margin:-2px 0 3px;color:#111}
.tight{font-size:6.7px;line-height:7.45px}
.indent1{padding-left:20px}
.highlight{background:var(--highlight-box);padding:4px 6px 4px 6px;margin:3px -6px 6px 14px}
.numbered{display:flex;gap:8px}
.footer-band{position:absolute;left:0;right:0;bottom:0;height:31px;background:var(--blue)}
</style>
</head>
<body>

<!-- Page 1: Charter cover -->
<section class="page p1">
  <header class="page-head"><div class="bar"></div><div class="title">The V20 Charter</div><div class="subtitle">A Corvane and Bramble Loop led initiative</div>
    <div class="brand-name">V20</div></header>
  <div class="pattern" style="left:0;top:300px;width:110px;height:130px" role="img" aria-label="Faint hexagon network decoration"></div>
  <div class="body" style="top:110px">
    <h1 class="slogan">"DIGITAL PARTICIPATION<br>FOR <span style="font-weight:800">THE VITAL 20%</span>"</h1>
    <h2 class="section-title">What is the V20 Charter?</h2>
    <p style="text-align:left">The V20 Charter is about ensuring Digital Participation for the global 'Vital 20%' led by Corvane and the nonprofit Bramble Loop.</p>
    <p style="text-align:left">More than 3 billion people remain unconnected, in many cases despite having access to internet. The number is disproportionately <span class="tag m">poor,</span><span class="tick">✓</span> <span class="tag m">rural,</span><span class="tick">✓</span> <span class="tag m">illiterate</span><span class="tick">✓</span> and <span class="tag m">female.</span><span class="tick">✓</span> The major challenges are cost, lack of digital skills, appropriate technology and applications relevant to local needs.</p>
    <p style="text-align:left"><span class="tag g">The V20 mission</span><span class="tick">✓</span> is to accelerate digital adoption and community enrichment through <span class="tag gr">innovative applications</span><span class="tick">✓</span> <span class="tag gr">network design</span><span class="tick">✓</span>and <span class="tag gr">business models</span><span class="tick">✓</span> to enable <span class="tag pl">the next 3.9 billion people</span><span class="tick">✓</span> <span class="tag pl">to participate in the digital world</span><span class="tick">✓</span></p>
    <p>V20 is a project driven, action led, collaboration between cross- industry global organisations, NGOs, Academic institutions and public and private sector entities seeking to enrich communities through implementing real world digital solutions.</p>
    <h2 class="section-title" style="margin-top:10px">Why support the V20 Charter?</h2>
    <p>There is a collective moral imperative to invest in each person's capacity for growth and opportunity. Access to affordable digital content, applications, and services at adequate speed is critical.</p>
    <p style="text-align:left">V20 already has live 'Digital Participation' projects in the field designed to enable communities to access the educational, health, social and financial benefits that flow from affordable and sustainable digital inclusion.</p>
    <p>V20 meets the needs of organizations and their staff to help address global Digital Equity through contributing projects, diverse skills, software and hardware technologies and solutions, community engagement and funding to real world projects.</p>
    <p>V20 and its ecosystem of partners will curate projects and help assemble partnerships, skills and funding to meet the needs of the community.</p>
  </div>
  <div class="cta-band">
    <h2>Why support the V20 Charter?</h2>
    <div>Simply sign the V20 Charter MOU below and return it to (<b>V20@brambleloop.org</b>)<br>To read more or to contact V20 staff, please visit (<b>www.v20.org</b>) or write to (<b>V20@brambleloop.org</b>)</div>
  </div>
</section>

<!-- Page 2: MOU -->
<section class="page p2">
  <header class="page-head"><div class="bar"></div><div class="title">The V20 Charter</div><div class="subtitle">A Corvane and Bramble Loop led initiative</div>
    <div class="brand-name">V20</div></header>
  <div class="body" style="top:88px;left:27px;right:36px;font-size:7px;line-height:8px">
    <h1 class="mou-title">MEMORANDUM OF UNDERSTANDING</h1>
    <div class="lead">This Memorandum of Understanding ("MOU") is entered into between:</div>
    <p>Bramble Loop, a 501(c)(3) nonprofit corporation, with its principal place of business at 14 Orchard Lane, Fairview VA, 22090 USA ("BL"); and</p>
    <p>[Company], a [type of company] with it principle place business at [Address] ("Company").</p>
    <p>The effective date of this MOU is [Date] ("Effective Date") and the expiration date of this MOU is [Date] ("Expiration Date").</p>
    <p>"CNDA" means the Corporate Non-Disclosure Agreement No. [CNDA reference number], dated [Date], entered into by the Parties.</p>
    <p style="margin-top:7px">In this MOU, BL and Company are sometimes referred to individually as a "Party" or collectively as "Parties."</p>
    <p style="margin-top:7px">BL and Company wish to record in writing their non-binding proposals regarding potential engagement(s), as described in the attached Schedule ("Engagement").</p>
    <table class="sign-table">
      <tr><th>For and on behalf of BL :</th><th>For and on behalf of Company :</th></tr>
      <tr><td style="padding-top:5px">By :</td><td style="padding-top:5px">By :</td></tr>
      <tr><td>Print Name :</td><td>Print Name :</td></tr>
      <tr><td>Title :</td><td>Title :</td></tr>
      <tr><td class="signed">Signed :</td><td class="signed">Signed :</td></tr>
      <tr><td>Date :</td><td>Date :</td></tr>
    </table>
    <div class="agree-title">THE PARTIES HEREBY AGREE AS FOLLOWS:</div>
    <ul class="clauses">
      <li><span class="n">1.</span><span>Non-Binding Nature: The Schedule to this MOU and its contents are not legally binding. Except for the obligations in Sections 1 to 10 and as specified in attached Exhibit A, which are all legally binding, no contract for the Engagement will exist unless and until the authorized representatives of each Party sign a separate legally binding written agreement.</span></li>
      <li><span class="n">2.</span><span>Term and Termination: This MOU will be effective on the Effective Date and will expire on the earlier of (a) the Expiration Date or (b) the date on which the Parties enter into a separate legally binding signed agreement relating to the Engagement. Either Party can, at any time for any reason and without any liability, end negotiations or terminate this MOU immediately upon giving written notice to the other Party. Sections 1, 2, 4, 8, and 9 of this MOU will survive termination of this MOU.]</span></li>
      <li><span class="n">3.</span><span>Expenses: Each Party is responsible for its own expenses in connection with all matters related to this MOU.</span></li>
    </ul>
  </div>
</section>

<!-- Page 3: MOU clauses -->
<section class="page p3">
  <header class="page-head"><div class="bar"></div><div class="title">The V20 Charter</div><div class="subtitle">A Corvane and Bramble Loop led initiative</div>
    <div class="brand-name">V20</div></header>
  <div class="body" style="top:65px;left:26px;right:38px">
    <ul class="clauses" style="font-size:6.6px">
      <li><span class="n">4.</span><span>Confidentiality and Public Announcement: Each Party must treat the other party's Confidential Information (as defined in the CNDA) in accordance with the CNDA identified on the first page of this MOU. The CNDA is a separate agreement and will survive the expiration or termination of this MOU. Neither Party will make any public announcement about the MOU (or the subject matter of this MOU), without the prior written consent of the other Party.</span></li>
      <li><span class="n">5.</span><span>License: No license is granted under this MOU to either Party under any of the other Party's intellectual property rights.</span></li>
      <li><span class="n">6.</span><span>Nature of relationship: The Parties are independent contractors, and no agency, partnership, franchise or joint venture is intended or created by this MOU. This MOU does not create an exclusive relationship between the Parties regarding the subject matter of this MOU.</span></li>
      <li><span class="n">7.</span><span>Entire Understanding: This MOU constitutes the entire understanding between the Parties regarding its subject matter. Neither Party has relied on any statements or representations made by the other in connection with this MOU, which are not set out in this MOU.</span></li>
      <li><span class="n">8.</span><span>Exclusion of Liability: Neither Party will have any liability whatsoever to the other Party under or in connection with this MOU or any Engagement, either in contract, tort or otherwise (including, without limitation, for negligence and misrepresentation), for: (a) loss of revenue; (b) loss of actual or anticipated profits; (c) loss of anticipated savings; (d) loss of reputation; (e) loss of, damage to or corruption of data; or (f) any indirect or consequential loss or damage howsoever arising. This exclusion of liability clause will not apply to any liability arising from breach of the obligations set out in Section 4 of this MOU.</span></li>
      <li><span class="n">9.</span><span>Governing Law &amp; Dispute Resolution: All disputes arising out of or related to this MOU, whether based on contract, tort, or any other legal or equitable theory, (a) will in all respects be governed by, and construed and interpreted under, the laws of the United States of America and the State of Delaware without reference to conflict of laws principles, and (b) will be subject to the exclusive jurisdiction of the courts of the State of Delaware or of the Federal courts sitting in that State. Each party submits to the personal jurisdiction of those courts and waives all objections to that jurisdiction and venue for those disputes.</span></li>
      <li><span class="n">10.</span><span>Language, Amendments and Severability: This MOU will be executed in English and the English language original of this MOU will prevail over any translation of it into any other languages. No amendments to this MOU will be effective unless made in writing and signed by authorized representatives of each Party. If any provision or part of these Sections 1 to 10 is held invalid or unenforceable under applicable law, the provision or part will be modified to the minimum extent necessary to make it valid and enforceable, or if it cannot be made valid and enforceable, the provision or part will be severed from this MOU.</span></li>
    </ul>
    <div class="exhibit-title">Exhibit A</div>
    <p class="tight" style="font-size:6.6px">The Vital 20 ("V20") is an alliance of Public, Private, NGO and Academic entities brought together to drive connectivity for the next 3.9 billion people who are isolated from participating in the digital connected world due to their rural location or socio-economic predicament. Member companies would collaborate to implement longer term communication infrastructure projects to include affordable broadband, WiFi and Internet services. V20 thought leaders would then join with local community members and businesses executives to mentor, train and help people in a sustainable manner to realize their potential and purpose both socially and economically.</p>
  </div>
</section>

<!-- Page 4: Schedule -->
<section class="page p4">
  <header class="page-head"><div class="bar"></div><div class="title">The V20 Charter</div><div class="subtitle">A Corvane and Bramble Loop led initiative</div>
    <div class="brand-name">V20</div></header>
  <div class="body tight" style="top:66px;left:25px;right:40px">
    <p>BL and Company agree to use commercially reasonable efforts to collaborate on V20 as described further below. It is understood that during the course of this collaboration, the Parties may further refine Phase definitions and would enter into a Definitive Agreement to advance the formation of the V20.</p>
    <div style="margin-bottom:6px">1. Definitions</div>
    <p class="indent1">"Founding Member" means initial V20 members committed to and involved in helping establish V20 in a phased approach via participation in V20 Project(s), input on V20 direction and helping enlist additional potential V20 members.</p>
    <p class="indent1" style="margin-top:6px">"Phase 1" means the series of activities between BL and the Founding Members to refine the scope, structure, and other aspects of V20 that would lead to the formation of official membership in the V20.</p>
    <p class="indent1" style="margin-top:6px">"Phase 2" means the series of activities between V20 and Founding Members that leads to participation in specific V20 charters/sponsored Projects.</p>
    <p class="highlight">"V20 Project" &amp; Sustainability Model to be considered a V20 Project the minimum fully loaded size is $500,000 in total project value per project. The maximum fiscal sponsorship fee to the V20 secretariat is $50 K per project. Depending on project scope and needs for Secretariat services and there are additional baskets of services available to members including: Enhanced Project Management Fee for additional services Per Project to be determined and agreed to on a case-by-case basis. Additional services may also include CSR/Impact/ESG/Theory of Change engagements.</p>
    <div style="padding-left:4px;margin-bottom:4px">2. Collaboration Scope</div>
    <p style="padding-left:11px">BL and Company will work together to make V20 a reality. Initial obligations are included below by Phase 1 (binding) and Phase 2 (non-binding). Phase 3 will be defined at an appropriate time after Phase 2 begins.</p>
    <div style="padding-left:11px;margin-bottom:4px">Phase 1 (Binding)</div>
    <div style="padding-left:25px;margin-bottom:2px">Company Obligations</div>
    <div class="numbered" style="padding-left:33px;margin-bottom:3px"><span>A.</span><span style="padding-left:10px">As part of Phase 1, the Company will:</span></div>
    <div style="padding-left:42px">
      <div class="numbered"><span>1.</span><span>meet with BL and Organization's personnel to explore full participation in V20.</span></div>
      <div class="numbered"><span>2.</span><span>provide feedback on V20 charter, scope and plans</span></div>
      <div class="numbered"><span>3.</span><span>identify potential Project(s) to participate in</span></div>
      <div class="numbered"><span>4.</span><span>describe potential areas for collaboration for Company and other V20 participants</span></div>
      <div class="numbered"><span>5.</span><span>agree to allow BL and Corvane to disclose Company interest as a Founding Member to other potential V20 Founding Members</span></div>
      <div class="numbered"><span>6.</span><span>Provide BL with the rights to use Company's logo on the V20 website and other V20 collateral to indicated Company's participation in V20</span></div>
    </div>
    <p style="padding-left:33px;margin-top:6px">B. &nbsp;&nbsp;&nbsp;Subject to satisfactory due diligence and management approval, Company, as a Founding Member of the V20, commits to:</p>
    <div style="padding-left:42px">
      <div class="numbered"><span>1.</span><span>help recruit additional members<br>provide feedback on V20 charter, scope and plans</span></div>
      <div class="numbered"><span>2.</span><span>participate in an existing initiative/Project underway by one or more of the Founding Members</span></div>
    </div>
  </div>
</section>

<!-- Page 5: Phase 2 -->
<section class="page p5">
  <header class="page-head"><div class="bar"></div><div class="title">The V20 Charter</div><div class="subtitle">A Corvane and Bramble Loop led initiative</div>
    <div class="brand-name">V20</div></header>
  <div class="body tight" style="top:66px;left:26px;right:40px;font-size:7px;line-height:7.6px">
    <div style="margin-bottom:6px">Phase 2 (Non-Binding)</div>
    <div style="padding-left:14px;margin-bottom:3px">Mutual Obligations</div>
    <div class="numbered" style="padding-left:22px;margin-bottom:3px"><span>A.</span><span style="padding-left:12px">As part of Phase 2, the Parties would:</span></div>
    <div style="padding-left:32px;margin-bottom:6px">
      <div class="numbered"><span>1.</span><span>meet with BL to determine the level of participation in V20</span></div>
      <div class="numbered"><span>2.</span><span>conclude appropriate Definitive Agreement for formal membership into V20</span></div>
    </div>
    <div class="numbered" style="padding-left:22px;margin-bottom:5px"><span>B.</span><span style="padding-left:12px">As part of Phase 2, the Company would:</span></div>
    <div style="padding-left:32px">
      <div class="numbered"><span>1.</span><span>participate in at least one V20 designated Project annually through the contribution of people, equipment or other resources</span></div>
    </div>
  </div>
  <div class="pattern" style="left:0;top:360px;width:150px;height:125px" role="img" aria-label="Faint hexagon network decoration"></div>
  <div class="footer-band"></div>
</section>

</body>
</html>
```